Yard Sign Design Needed

Yard sign needed for mowing & landscaping company. Would like to use the top logo with black background which is attached. Would like MOWING to be in large standout letters. The word "landscaping" can be smaller and more artistic or omitted. Will need room for phone number once design is approved. The phone number will need to stand out and look identical/similar to the word 'MOWING"

```html
<!DOCTYPE html>
<html lang="en">
<head>
<meta charset="utf-8">
<title>Brenwick Contractors – Mowing Yard Sign</title>
<link href="https://fonts.googleapis.com/css2?family=Montserrat:wght@600;700;800&display=swap" rel="stylesheet">
<style>
  :root {
    --sign-black: #000000;
    --sign-white: #ffffff;
    --brand-green: #8fa80a;
    --page-bg: #ececec;
  }
  * { margin: 0; padding: 0; box-sizing: border-box; }
  html, body {
    width: 1075px;
    height: 1200px;
    overflow: hidden;
    background: var(--page-bg);
    font-family: "Montserrat", Arial, sans-serif;
  }
  .yard-sign {
    position: absolute;
    left: 37px;
    top: 200px;
    width: 1000px;
    height: 800px;
    display: flex;
    flex-direction: column;
    background: var(--sign-white);
  }
  .brand-band {
    height: 264px;
    flex: none;
    background: var(--sign-black);
    display: flex;
    align-items: center;
    justify-content: center;
    gap: 24px;
  }
  .brand-mark {
    width: 72px;
    height: 72px;
    background: var(--brand-green);
  }
  .brand-name {
    color: var(--brand-green);
    font-weight: 700;
    font-size: 44px;
    line-height: 1.1;
    letter-spacing: 3px;
    text-transform: uppercase;
  }
  .brand-name span { display: block; }
  .service-panel {
    height: 332px;
    flex: none;
    position: relative;
  }
  .service-main {
    position: absolute;
    left: 0;
    right: 0;
    top: 22px;
    text-align: center;
    color: var(--brand-green);
    font-weight: 800;
    font-size: 174px;
    line-height: 1;
    letter-spacing: -1px;
  }
  .service-bar {
    position: absolute;
    left: 86px;
    top: 189px;
    width: 828px;
    height: 87px;
    background: var(--brand-green);
    display: flex;
    align-items: center;
    justify-content: center;
  }
  .service-sub {
    color: var(--sign-white);
    font-weight: 700;
    font-size: 68px;
    letter-spacing: 0;
    line-height: 1;
  }
  .divider {
    height: 5px;
    flex: none;
    background: var(--brand-green);
    position: relative;
  }
  .phone-badge {
    position: absolute;
    left: 466px;
    top: -32px;
    width: 68px;
    height: 68px;
    border-radius: 50%;
    background: var(--sign-white);
    border: 4px solid var(--brand-green);
    display: flex;
    align-items: center;
    justify-content: center;
    z-index: 1;
  }
  .contact-band {
    flex: 1;
    background: var(--sign-black);
    display: flex;
    align-items: center;
    justify-content: center;
  }
  .phone-number {
    color: var(--sign-white);
    font-weight: 800;
    font-size: 130px;
    line-height: 1;
    letter-spacing: -2px;
    word-spacing: 4px;
    margin-top: 16px;
  }
</style>
</head>
<body>
  <main class="yard-sign">
    <header class="brand-band">
      <div class="brand-mark"></div>
      <div class="brand-name">
        <span>Brenwick</span>
        <span>Contractors LLC</span>
      </div>
    </header>
    <section class="service-panel">
      <h1 class="service-main">MOWING</h1>
      <div class="service-bar">
        <h2 class="service-sub">LANDSCAPING</h2>
      </div>
    </section>
    <div class="divider">
      <div class="phone-badge">
        <svg width="32" height="34" viewBox="0 0 24 24" aria-hidden="true">
          <path fill="#8fa80a" d="M6.6 10.8c1.4 2.8 3.8 5.1 6.6 6.6l2.2-2.2c.3-.3.7-.4 1-.2 1.1.4 2.3.6 3.6.6.6 0 1 .4 1 1V20c0 .6-.4 1-1 1C10.6 21 3 13.4 3 4c0-.6.4-1 1-1h3.5c.6 0 1 .4 1 1 0 1.3.2 2.5.6 3.6.1.3 0 .7-.2 1L6.6 10.8z"/>
        </svg>
      </div>
    </div>
    <footer class="contact-band">
      <p class="phone-number">0420 318 657</p>
    </footer>
  </main>
</body>
</html>
```